personal one page website

personal one page site. based on details available on www.drlucasferrow.com
design needs to show:
- unique background of doctor
- serving high value customer group
- non-profit work
if you would compare the professional life of DrLucasFerrow with other brands:
a car: it would be velmor crade
a watch: it would be Quorin Velsaud
a sport: horse polo
a sports gear company: zolt
a drink: macha green tea
a city: Tokyo
the visitor of the site should have the following impressions (in chronological order):
1. Beautiful
2. Interesting
3. this person is a good example for others
4. what will be next ?
www.drlucasferrow.com
the main colors should be black / white / grey scales. thank you (including photos).
dear all. the site serves information purpose only and is non-commercial (no phone, appointment, twitter ,fb on the site). you can look at it as an 'online-CV'. no link to the company site 'harbimedic.com'
Dear All,

```html
<!DOCTYPE html>
<html lang="en">
<head>
<meta charset="utf-8">
<title>Doctor Lucas A Ferrow, PhD</title>
<link rel="stylesheet" href="https://fonts.googleapis.com/css2?family=Magra:wght@400;700&family=Open+Sans:wght@400;600&display=swap">
<style>
:root{
  --page:#141414;
  --nav:#0c0c0c;
  --gold:#b58a2a;
  --gold-light:#d3a23a;
  --panel:#e2e2e0;
  --ink:#3c3c3c;
  --muted:#555;
  --rule:#8a8a8a;
  --footer:#2e2e2e;
  --white:#fff;
}
*{margin:0;padding:0;box-sizing:border-box}
html,body{width:744px;height:1200px;overflow:hidden;background:var(--page);font-family:"Open Sans",sans-serif;color:var(--ink)}
.canvas{position:relative;width:744px;height:1200px}
.abs{position:absolute}
.portrait{left:140px;top:0;width:175px;height:181px;background:radial-gradient(ellipse at 45% 45%,#b89a86 0%,#8a7466 35%,#4a403a 65%,#141414 100%);border-radius:0 0 40px 40px}
.site-title{left:298px;top:76px;font-family:"Magra",sans-serif;font-size:25px;color:var(--white);letter-spacing:.3px}
.site-sub{left:298px;top:112px;font-family:"Magra",sans-serif;font-size:12px;color:#eee}
.nav{left:106px;top:181px;width:532px;height:45px;background:linear-gradient(#1e1e1e,var(--nav));display:flex}
.nav a{font-family:"Magra",sans-serif;font-size:10px;font-weight:700;color:#ececec;text-decoration:none;height:45px;line-height:45px;text-align:center}
.nav .current{background:linear-gradient(#d8a640,var(--gold));color:#2a1d05;width:67px}
.slider{left:106px;top:226px;width:532px;height:266px;background:linear-gradient(160deg,#d8d6d0 0%,#a59c8f 40%,#6b6156 70%,#c9ccd2 100%)}
.caption{left:30px;top:173px;width:305px;height:46px;background:rgba(0,0,0,.55);color:#fff;font-size:9.5px;line-height:19px;padding:4px 10px}
.arrow{top:136px;width:12px;height:12px;border-radius:50%;background:rgba(0,0,0,.35)}
.dots{left:0;width:532px;top:251px;display:flex;justify-content:center;gap:14px;padding-left:8px}
.dots span{width:6px;height:6px;border-radius:50%;background:#ddd}
.dots span:first-child{background:#fff}
.content{left:106px;top:492px;width:532px;height:633px;background:var(--panel)}
.rule{left:0;width:532px;border-top:1px dashed var(--rule)}
.welcome{left:14px;top:30px;font-family:"Magra",sans-serif;font-weight:700;font-size:21px;color:var(--gold)}
.welcome-text{left:126px;top:27px;width:392px;font-size:6.6px;line-height:13px;color:var(--muted)}
.feature{width:150px;text-align:center}
.feature svg{display:block;margin:0 auto}
.feature h3{font-family:"Magra",sans-serif;font-weight:400;font-size:12px;color:#555;margin-top:6px}
.feature.active h3{color:var(--gold)}
.feature p{font-size:6.4px;line-height:16px;color:#444;margin-top:6px}
.pubs{left:6px;top:296px;width:360px}
.pubs h2{font-family:"Magra",sans-serif;font-size:8.6px;font-weight:400;color:#222;text-decoration:underline;text-underline-offset:2px}
.pubs ol{list-style:none;margin:4px 0 0 8px}
.pubs li{font-size:7px;line-height:12.5px;color:#666;margin-bottom:7px}
.btn{background:#111;color:#fff;font-size:7px;display:flex;align-items:center;justify-content:center}
.video-box{left:360px;top:297px;width:166px;height:118px;background:#e8e8e6;border:1px solid #d0d0cc}
.video-box h4{position:absolute;left:11px;top:11px;font-family:"Magra",sans-serif;font-weight:400;font-size:9px;color:#333}
.video{position:absolute;left:11px;top:27px;width:146px;height:82px;background:linear-gradient(#bcc3c9,#6f6f70 60%,#2a2a2a);}
.video .bar{position:absolute;left:0;top:0;width:100%;height:10px;background:rgba(0,0,0,.8);color:#ddd;font-size:4px;line-height:10px;padding-left:4px}
.video .ctrl{position:absolute;left:0;bottom:0;width:100%;height:10px;background:#111}
.video .play{position:absolute;left:65px;top:35px;width:16px;height:12px;border-radius:3px;background:rgba(0,0,0,.7)}
.gallery-label{left:9px;top:440px;font-family:"Magra",sans-serif;font-size:9px;color:#333}
.thumb{width:121px;height:68px}
.footer{left:106px;top:1125px;width:532px;height:57px;background:var(--footer)}
.footer-links{left:8px;top:14px;font-size:6px;color:#eee}
.copy{left:8px;top:37px;font-size:5px;color:#999}
.social{right:8px;top:21px;display:flex;gap:4px}
.social span{width:17px;height:17px;border-radius:4px;background:#6a6a6a}
</style>
</head>
<body>
<div class="canvas">
  <div class="abs portrait" role="img" aria-label="Portrait photo of the doctor"></div>
  <h1 class="abs site-title">Doctor Lucas A Ferrow, PhD</h1>
  <p class="abs site-sub">Doctor of Dental Surgery (West-Germany)</p>

  <nav class="abs nav">
    <a class="current" href="#">Home</a>
    <a href="#" style="width:63px">About Us</a>
    <a href="#" style="width:65px">Gallery</a>
    <a href="#" style="width:57px">Media</a>
    <a href="#" style="width:50px">Blog</a>
    <a href="#" style="width:76px">Contact Us</a>
  </nav>

  <section class="abs slider" role="img" aria-label="Photo of the doctor with a medical team beside a mobile dental care unit">
    <div class="abs arrow" style="left:6px"></div>
    <div class="abs arrow" style="right:6px"></div>
    <div class="abs caption">Proudly supporting the strong team and patients from Abu Dhabi and Al Ain</div>
    <div class="abs dots"><span></span><span></span><span></span><span></span><span></span></div>
  </section>

  <main class="abs content">
    <h2 class="abs welcome">WELCOME</h2>
    <p class="abs welcome-text">Lorem ipsum dolor sit amet, consectetur adipiscing elit, sed do eiusmod tempor incididunt ut labore et dolore magna aliqua. Ut enim ad minim veniam, quis nostrud exercitation ullamco laboris nisi ut aliquip ex ea commodo. Lorem ipsum dolor sit amet, consectetur adipiscing.</p>
    <div class="abs rule" style="top:83px"></div>

    <div class="abs feature active" style="left:20px;top:113px">
      <svg width="60" height="60" viewBox="0 0 60 60"><circle cx="30" cy="30" r="28.5" fill="none" stroke="var(--gold)" stroke-width="1.6"/><rect x="18" y="22" width="24" height="18" rx="2" fill="var(--gold-light)"/><rect x="25" y="18" width="10" height="5" rx="1" fill="none" stroke="var(--gold-light)" stroke-width="2"/><path d="M30 26v10M25 31h10" stroke="#fff" stroke-width="3"/></svg>
      <h3>Best Service</h3>
      <p>Lorem ipsum dolor sit amet, consectetur adipiscing elit, Lorem ipsum dolor sit amet, consectetuer adipiscing elit.</p>
    </div>
    <div class="abs feature" style="left:191px;top:113px">
      <svg width="60" height="60" viewBox="0 0 60 60"><circle cx="30" cy="30" r="28.5" fill="none" stroke="#555" stroke-width="1.6"/><path d="M17 30c7-9 19-9 26 0c-7 9-19 9-26 0z" fill="#555"/><circle cx="30" cy="30" r="5" fill="var(--panel)"/><circle cx="30" cy="30" r="2.5" fill="#555"/></svg>
      <h3>High Value Customers</h3>
      <p>Lorem ipsum dolor sit amet, consectetuer adipiscing elit, Lorem ipsum dolor sit amet, consectetuer adipiscing elit.</p>
    </div>
    <div class="abs feature" style="left:366px;top:113px">
      <svg width="60" height="60" viewBox="0 0 60 60"><circle cx="30" cy="30" r="28.5" fill="none" stroke="#555" stroke-width="1.6"/><path d="M30 18c-4 7-8 11-8 16a8 8 0 0 0 16 0c0-5-4-9-8-16z" fill="#555"/></svg>
      <h3>Non-Profit Services</h3>
      <p>Lorem ipsum dolor sit amet, consectetuer adipiscing elit, Lorem ipsum dolor sit amet, consectetuer adipiscing elit.</p>
    </div>
    <div class="abs rule" style="top:280px"></div>

    <section class="abs pubs">
      <h2>Scientific Publications in Journals and on Conferences (24) by Dr Lucas Ferrow</h2>
      <ol>
        <li>1. Review of Lingual Orthodontics, 2/1999: Self Ligating Brackets in Lingual Orthodontics<br>(with RM Ostrander)</li>
        <li>2. Halbrook School of Dental Medicine 9/1995: Dental Education in Germany</li>
        <li>3. Global Society for Oral Research 3/1999: Material Properties of latex-free intraoral<br>elastics (with RM Ostrander)</li>
      </ol>
    </section>
    <a class="abs btn" style="left:16px;top:397px;width:44px;height:18px">View All</a>

    <aside class="abs video-box">
      <h4>Latest Video</h4>
      <div class="video" role="img" aria-label="Video still of the doctor in a clinic">
        <div class="bar">Dental Clinic Visit Video Clip</div>
        <div class="play"></div>
        <div class="ctrl"></div>
      </div>
    </aside>
    <div class="abs rule" style="top:429px"></div>

    <h2 class="abs gallery-label">Photo Gallery</h2>
    <a class="abs btn" style="left:482px;top:437px;width:44px;height:18px">View All</a>

    <div class="abs thumb" style="left:7px;top:466px;background:linear-gradient(135deg,#8d8f93,#d6d3cc,#6f6c68)" role="img" aria-label="Photo of the doctor meeting a guest"></div>
    <div class="abs thumb" style="left:139px;top:466px;background:linear-gradient(135deg,#e5e4e0,#b7a397,#d9d8d6)" role="img" aria-label="Portrait photo of the doctor"></div>
    <div class="abs thumb" style="left:271px;top:466px;background:linear-gradient(135deg,#6a4b44,#a08c86,#3a3a48)" role="img" aria-label="Photo of a dental treatment"></div>
    <div class="abs thumb" style="left:402px;top:466px;background:linear-gradient(135deg,#cfd0d2,#7b7466,#b9bfcb)" role="img" aria-label="Photo of the doctor with a team outdoors"></div>
    <div class="abs thumb" style="left:7px;top:546px;background:linear-gradient(135deg,#c9cad0,#5b5d6a,#a3a6b0)" role="img" aria-label="Photo of a group beside a mobile clinic"></div>
    <div class="abs thumb" style="left:139px;top:546px;background:linear-gradient(135deg,#5a5148,#b4936d,#4a4e55)" role="img" aria-label="Photo of the doctor in surgical cap"></div>
    <div class="abs thumb" style="left:271px;top:546px;background:linear-gradient(135deg,#3b3a3c,#a07c70,#2b2b30)" role="img" aria-label="Photo of dentists at work"></div>
    <div class="abs thumb" style="left:402px;top:546px;background:linear-gradient(135deg,#8cb2cf,#3f5f7b,#c9c2b4)" role="img" aria-label="Photo of runners at a charity race"></div>
  </main>

  <footer class="abs footer">
    <p class="abs footer-links">Sitemap &nbsp;| &nbsp;Terms and Conditions | Privacy &amp; Policy &nbsp;| Contact Us</p>
    <p class="abs copy">Copyright 2014 - drlucasferrow. All rights reserved.</p>
    <div class="abs social"><span></span><span></span><span></span><span></span><span></span><span></span></div>
  </footer>
</div>
</body>
</html>
```